Benefits of Supplement Infographic - character illustration of health benefits

we are a supplement company who want to have an infographic that shows the benefits of the supplement, We have a few key areas which we have sketched out and have also included an excel spreadsheet with some detail that relates to the visual attached. Obviously these are very high level concepts, please reach out to me with any questions.

Target Market(s)

Our customers will be affluent millennials and adults who are health conscious also frontline workers e.g. police, firemen, doctors, nurses who want to boost immunity.

Font styles to use
Sans Serif

Colors
3176b5
876aae
9bcb3c

Requirements
Must have
• General: Characters need to be illustrations, match stick men would be ideal. Want it to be playful.
Athletes: 2 people running.
Lifestyle Stress: Person sitting at desk on laptop, lightening emblems at head to represent stress.
Physical stress: Firefighter character needed as study was on firefighter population.
Children: Children playing, skipping rope ideal.
Elderly: 2 characters on bikes will suffice here.

```html
<!DOCTYPE html>
<html lang="en">
<head>
<meta charset="UTF-8">
<title>Supplement Benefits Infographic</title>
<link href="https://fonts.googleapis.com/css2?family=Exo+2:wght@400;800&display=swap" rel="stylesheet">
<style>
  :root {
    --teal: #52a28e;
    --plum: #a5508f;
    --ink: #3a3a3a;
    --frame: #474747;
    --divider: #3f3f3f;
    --paper: #ffffff;
  }
  * { margin: 0; padding: 0; box-sizing: border-box; }
  html, body {
    width: 1200px;
    height: 394px;
    overflow: hidden;
    background: var(--paper);
  }
  .infographic {
    position: relative;
    width: 1200px;
    height: 394px;
    border: 1.5px solid var(--frame);
    font-family: "Exo 2", sans-serif;
  }
  .benefit {
    position: absolute;
    top: 0;
    width: 200px;
    height: 394px;
    margin-left: -100px;
    text-align: center;
  }
  .benefit__title {
    position: absolute;
    left: 0;
    right: 0;
    color: var(--teal);
    font-weight: 800;
    font-size: 27px;
    line-height: 24px;
    letter-spacing: 0.5px;
  }
  .benefit__title--single { top: 106px; }
  .benefit__title--double { top: 104px; }
  .benefit__figure {
    position: absolute;
    left: 50%;
    top: 164px;
    height: 78px;
    transform: translateX(-50%);
    border-radius: 10px;
    background: linear-gradient(180deg, #4a4a4a, var(--ink));
  }
  .benefit__stat {
    position: absolute;
    left: 0;
    right: 0;
    top: 244px;
    color: var(--plum);
    font-size: 18px;
    line-height: 22px;
    font-weight: 400;
  }
  .benefit__stat strong { font-weight: 800; }
  .divider {
    position: absolute;
    top: 105px;
    width: 2px;
    height: 177px;
    background: var(--divider);
  }
</style>
</head>
<body>
<main class="infographic">
  <section class="benefit" style="left:178px">
    <h2 class="benefit__title benefit__title--single">ATHLETES</h2>
    <div class="benefit__figure" style="width:110px" role="img" aria-label="Two stick figures running"></div>
    <p class="benefit__stat"><strong>40%</strong> Reduction in<br>URTI Symptoms</p>
  </section>
  <div class="divider" style="left:286px"></div>

  <section class="benefit" style="left:397px">
    <h2 class="benefit__title benefit__title--double">LIFETIME<br>STRESS</h2>
    <div class="benefit__figure" style="width:46px" role="img" aria-label="Stressed stick figure holding head with lightning marks"></div>
    <p class="benefit__stat"><strong>70%</strong> Reduction in<br>URTI Days</p>
  </section>
  <div class="divider" style="left:500px"></div>

  <section class="benefit" style="left:601px">
    <h2 class="benefit__title benefit__title--double">PHYSICAL<br>STRESS</h2>
    <div class="benefit__figure" style="width:40px" role="img" aria-label="Tired figure with a low battery above the head"></div>
    <p class="benefit__stat"><strong>23%</strong> Reduction in<br>URTI Days</p>
  </section>
  <div class="divider" style="left:705px"></div>

  <section class="benefit" style="left:810px">
    <h2 class="benefit__title benefit__title--single" style="top:110px">CHILDREN</h2>
    <div class="benefit__figure" style="width:96px" role="img" aria-label="Two children jumping and playing"></div>
    <p class="benefit__stat"><strong>6</strong> fever Sick<br>Days</p>
  </section>
  <div class="divider" style="left:911px"></div>

  <section class="benefit" style="left:1006px">
    <h2 class="benefit__title benefit__title--single">ELDERLY</h2>
    <div class="benefit__figure" style="width:76px" role="img" aria-label="Elderly couple standing, one with a cane"></div>
    <p class="benefit__stat"><strong>16%</strong> Reduction in<br>URTI Days</p>
  </section>
</main>
</body>
</html>
```